Single Sided 1 Page Tour Flyer in the same theme as previous brochure

We need a single sided 8.5 x 11 flyer in the same theme and color scheme as the previous brochure we worked on together. the flyer should include the following

1. company logo up top (just like on the front panel of previous brochure
2. tour name "Maple & Pine Highlights" also on the top
3. a large photo towards the top of the flyer, similar to the brochure front
4. 3 panels of text: left one for tour prices, whats included, additional notes, center and right panels for tour program details (day 1, day 2, etc)
5. below that, a few lines for additional details, like small print and stuff
6. company address, phone numbers, email address, and website link
6. below that a banner of small photos, maybe 4 in a row, similar to the brochure

details of the actual tour can be found at this link:
http://bluepebbletrips.ru/en/tours/maple-and-pine-11-days/

once again, we would love for the flyer to be in the same theme and style as the other brochure, so it matches, we loved the previous work!!

```html
<!DOCTYPE html>
<html lang="en">
<head>
<meta charset="utf-8">
<title>Maple &amp; Pine Highlights – Blue Pebble Trips</title>
<link rel="stylesheet" href="https://fonts.googleapis.com/css2?family=PT+Sans:ital,wght@0,400;0,700;1,700&family=PT+Sans+Narrow:wght@400;700&display=swap">
<style>
:root{
  --red:#d2232a;
  --red-dark:#b5161d;
  --gold:#f2b705;
  --ink:#231f20;
  --grey:#58595b;
  --bar:#3b3b3d;
  --paper:#ffffff;
}
*{margin:0;padding:0;box-sizing:border-box}
html,body{width:887px;height:1200px;overflow:hidden;background:var(--paper)}
body{font-family:"PT Sans",Arial,sans-serif;color:var(--ink);position:relative}
.flyer{position:relative;width:887px;height:1200px;overflow:hidden;background:var(--paper)}

/* header */
.brand{position:absolute;left:36px;top:40px;display:flex;align-items:center;gap:12px}
.brand-dot{width:54px;height:54px;border-radius:50%;background:var(--gold)}
.brand-name{font-weight:700;font-size:33px;color:var(--grey);letter-spacing:.5px}
.tour-title{position:absolute;right:40px;top:52px;font-family:"PT Sans Narrow",Arial,sans-serif;font-weight:700;font-size:36px;color:var(--ink)}

.header-swoosh{position:absolute;left:0;top:100px;width:887px;height:60px}
.hero{position:absolute;left:0;top:122px;width:887px;height:370px;
  background:linear-gradient(180deg,#2c2a5c 0%,#4a4a86 35%,#6b5f92 55%,#c9733f 66%,#3d3561 72%,#1e1c40 100%)}
.hero-swoosh{position:absolute;left:0;top:418px;width:887px;height:100px}

/* destinations */
.destinations{position:absolute;left:30px;top:514px;display:flex;align-items:center;gap:10px}
.destinations .dot{width:30px;height:30px;border-radius:50%;background:var(--gold)}
.destinations p{font-weight:700;font-style:italic;font-size:15.5px;color:var(--ink);letter-spacing:.2px}

/* left column */
.pricing{position:absolute;left:30px;top:570px;width:240px}
.from{font-size:14px;display:flex;align-items:flex-start;gap:8px}
.from strong{font-family:"PT Sans Narrow",Arial,sans-serif;font-weight:400;font-size:30px;line-height:1;margin-top:-10px}
.from strong sup{font-size:17px}
.fares{display:flex;justify-content:space-between;margin-top:10px;width:222px}
.fare span{display:block;font-weight:700;font-size:19px;line-height:1}
.fare b{font-weight:700;font-size:15px}
.fare.single span,.fare.triple span{color:var(--red)}
.fare-note{font-size:8px;margin-top:6px}
.notes{margin-top:14px;font-size:11px;line-height:1.3}
.notes p+p{margin-top:9px}

.included{position:absolute;left:30px;top:803px;width:250px}
.included h2{background:var(--red);color:#fff;font-family:"PT Sans Narrow",Arial,sans-serif;font-weight:700;font-size:19px;padding:2px 10px;border-radius:0 14px 14px 0;letter-spacing:.3px}
.included ul{list-style:none;margin-top:8px}
.included li{font-size:10.5px;font-weight:700;line-height:1.5;padding-left:16px;position:relative}
.included li::before{content:"";position:absolute;left:2px;top:5px;width:8px;height:8px;border-radius:50%;background:var(--red)}

/* itinerary */
.itinerary-head{position:absolute;left:290px;top:574px;width:146px;background:var(--red);color:#fff;
  font-family:"PT Sans Narrow",Arial,sans-serif;font-weight:700;font-size:19px;padding:1px 10px;border-radius:0 14px 14px 0}
.itinerary-col{position:absolute;top:609px;display:flex;flex-direction:column}
.col-a{left:290px;width:268px;gap:9px}
.col-b{left:573px;width:282px;gap:6px}
.day{font-size:10.5px;line-height:1.3}
.day h3{font-weight:700;font-size:13.5px;color:var(--red);line-height:1.1;margin-bottom:1px}

.small-print{position:absolute;left:290px;top:926px;width:570px;font-size:7.2px;line-height:1.2;color:var(--grey)}

/* photo strip */
.strip-swoosh{position:absolute;left:0;top:940px;width:887px;height:60px}
.strip{position:absolute;left:0;top:980px;width:887px;height:165px;display:flex}
.strip .shot{height:100%}
.shot-falls{width:250px;background:linear-gradient(180deg,#6d8fb4,#d9e4ee 45%,#3f6e3a)}
.shot-room{width:183px;background:linear-gradient(135deg,#7a4a2a,#c99a62 55%,#e8d3a8)}
.shot-liberty{width:133px;background:linear-gradient(180deg,#2f65b8,#5f93cf 50%,#7fa89a)}
.shot-capitol{width:164px;background:linear-gradient(180deg,#1f2c5e,#3b4d8c 50%,#a4693c)}
.shot-ship{width:157px;background:linear-gradient(180deg,#3a7bd0,#8fb9e8 55%,#1c4f86)}

.address{position:absolute;left:0;top:1145px;width:887px;height:24px;background:var(--bar);color:#e8e8e8;
  font-size:11px;letter-spacing:3.4px;text-align:center;line-height:24px}
.contacts{position:absolute;left:0;top:1169px;width:887px;height:31px;background:var(--red-dark);color:#fff;
  display:flex;justify-content:center;gap:58px;align-items:center;font-size:14px;font-weight:700}
.contacts span{display:flex;align-items:center;gap:7px}
.contacts svg{width:18px;height:14px}
</style>
</head>
<body>
<div class="flyer">

  <header>
    <div class="brand"><span class="brand-dot"></span><span class="brand-name">Blue Pebble Trips</span></div>
    <h1 class="tour-title">Maple &amp; Pine Highlights</h1>
  </header>

  <div class="hero" role="img" aria-label="Night photograph of a lit suspension bridge over the bay with a city skyline at dusk"></div>

  <svg class="header-swoosh" viewBox="0 0 887 60" preserveAspectRatio="none" aria-hidden="true">
    <path d="M0 22 C250 0 600 0 887 30 L887 0 L0 0Z" fill="#fff"/>
    <path d="M0 22 C250 0 600 0 887 30 L887 36 C600 8 250 8 0 28Z" fill="#f2b705"/>
  </svg>

  <svg class="hero-swoosh" viewBox="0 0 887 100" preserveAspectRatio="none" aria-hidden="true">
    <path d="M0 70 C300 40 600 40 887 0 L887 100 L0 100Z" fill="#fff"/>
    <path d="M0 66 C300 36 600 36 887 -4 L887 6 C600 46 300 46 0 76Z" fill="#f2b705"/>
    <path d="M0 78 C300 52 600 52 887 14 L887 18 C600 58 300 58 0 82Z" fill="#d0d0d2"/>
  </svg>

  <div class="destinations"><span class="dot"></span><p>NEW YORK, WASHINGTON, D.C., PHILADELPHIA, BOSTON, MONTREAL, QUEBEC, OTTAWA, NIAGARA FALLS</p></div>

  <section class="pricing">
    <div class="from">Cost for 1 person from <strong><sup>$</sup>1,495</strong></div>
    <div class="fares">
      <div class="fare double"><span>DBL</span><b>$1,395</b></div>
      <div class="fare single"><span>SNGL</span><b>$1,395</b></div>
      <div class="fare triple"><span>TRPL</span><b>$1,995</b></div>
    </div>
    <p class="fare-note">(Personalise in process of purchasing)</p>
    <div class="notes">
      <p>*Departure from Buffalo Airport (BUF) is also possible (transfer is not included in the program, and is an additional charge)</p>
      <p>Participants can also return to New York, Manhattan, or JFK Airport (transfer is free). Departure from JFK airport is not possible on the 11th Day due to time constraints.</p>
    </div>
  </section>

  <section class="included">
    <h2>INCLUDED IN PRICE:</h2>
    <ul>
      <li>Double occupancy in hotels along the route</li>
      <li>Breakfasts</li>
      <li>Excursions as per itinerary</li>
    </ul>
  </section>

  <h2 class="itinerary-head">TOUR ITINERARY:</h2>

  <div class="itinerary-col col-a">
    <div class="day"><h3>Day 1</h3>Arrival to Washington, D.C., registration in hotel. Overnight in Washington, D.C.</div>
    <div class="day"><h3>Day 2</h3>Sightseeing tour of Washington, D.C.: memorials, Capitol Building, White House, museums, and much more. Overnight in Washington, D.C.</div>
    <div class="day"><h3>Day 3</h3>Departure to Philadelphia. Sightseeing tour of Philadelphia. Departure to New York, leisure time in the evening. Overnight in New York</div>
    <div class="day"><h3>Day 4</h3>Sightseeing tour of New York: Manhattan, Wall Street, United Nations Building, Broadway, Times Square. *optional cruise to the Statue of Liberty and Ellis Island. Overnight in New York</div>
    <div class="day"><h3>Day 5</h3>Departure to Boston. Sightseeing tour of Boston, Harvard University. Overnight in Boston</div>
  </div>

  <div class="itinerary-col col-b">
    <div class="day"><h3>Day 6</h3>Departure to Montreal, sightseeing tour of the city. Overnight in Montreal</div>
    <div class="day"><h3>Day 7</h3>Sightseeing tour of Quebec, return to Montreal. Overnight in Montreal</div>
    <div class="day"><h3>Day 8</h3>Second part of sightseeing tour of Montreal. Old Town, Montreal Port, Notre Dame de Montreal. Departure to Ottawa, sightseeing tour of Ottawa. Overnight in Ottawa</div>
    <div class="day"><h3>Day 9</h3>Departure to Rockport, cruise of 1,000 Islands, Departure to Toronto. Overnight in Toronto</div>
    <div class="day"><h3>Day 10</h3>Sightseeing tour of Toronto. Departure to Niagara Falls. Cruise to the Niagara Falls. Overnight in Niagara Falls</div>
    <div class="day"><h3>Day 11</h3>Transfer to Toronto Airport (YYZ). End of tour program</div>
  </div>

  <p class="small-print">*We recommend extending your trip with additional nights in New York, for leisure time in Manhattan, Broadway shows, shopping, and much more.<br>*We recommend extending your trip with additional nights in New York, for leisure time in Manhattan, Broadway shows, shopping, and much more.</p>

  <svg class="strip-swoosh" viewBox="0 0 887 60" preserveAspectRatio="none" aria-hidden="true">
    <path d="M0 40 C300 10 600 10 887 30 L887 60 L0 60Z" fill="#3b3b3d"/>
    <path d="M0 34 C300 2 600 2 887 22 L887 30 C600 12 300 12 0 42Z" fill="#d2232a"/>
  </svg>

  <div class="strip">
    <div class="shot shot-falls" role="img" aria-label="Photo of a wide waterfall surrounded by green forest"></div>
    <div class="shot shot-room" role="img" aria-label="Photo of a warm hotel room interior with a balcony"></div>
    <div class="shot shot-liberty" role="img" aria-label="Photo of a green copper statue monument against a blue sky"></div>
    <div class="shot shot-capitol" role="img" aria-label="Photo of a domed capitol building at dusk with city lights"></div>
    <div class="shot shot-ship" role="img" aria-label="Photo of a white cruise ship on blue water"></div>
  </div>

  <footer>
    <p class="address">Blue Pebble Trips, Inc. 1450 Harbor View Ave. Suite #310. Portland, OR 97201</p>
    <div class="contacts">
      <span><svg viewBox="0 0 18 14" aria-hidden="true"><rect x="1" y="1" width="16" height="12" fill="#f2b705"/><path d="M1 1 L9 8 L17 1" fill="none" stroke="#b5161d" stroke-width="1.5"/></svg>info@bluepebbletrips.com</span>
      <span><svg viewBox="0 0 18 14" aria-hidden="true"><path d="M4 1 C2 1 1 3 2 5 C4 9 7 12 11 13 C13 13.5 15 12 15 10 L12 8 L10 9.5 C8 8.5 6 6.5 5 4.5 L6.5 3Z" fill="#f2b705"/></svg>1(800)555-0142</span>
      <span><svg viewBox="0 0 18 14" aria-hidden="true"><circle cx="9" cy="7" r="6" fill="none" stroke="#f2b705" stroke-width="1.5"/><path d="M3 7 H15 M9 1 C6 4 6 10 9 13 M9 1 C12 4 12 10 9 13" fill="none" stroke="#f2b705" stroke-width="1.2"/></svg>www.http://bluepebbletrips.com</span>
    </div>
  </footer>

</div>
</body>
</html>
```